This is a label for a new sake made in Japan imported into Aust

This will be a bottle label for a new sake imported into Australia. The hero of the label is the Velmora. We have joined the "O" meaning great in Japanese and used sake with "Z" to have Velmora with the play on words using Oz as in our slang for Aussie. A modern label with a Japanese take is key. This is a premium sake made in Japan for the Australian market.
The "Tall Casks" up the top is the name of the company, we have yet to design a logo for the company.

Target Market(s)

Alcohol

Logo Text

Velmora

Font styles to use
Serif

Requirements
Must have
• easy to read, with a hint of Japanese origin
Should not have
• too busy

```html
<!DOCTYPE html>
<html lang="en">
<head>
<meta charset="utf-8">
<title>Velmora sake label</title>
<link rel="stylesheet" href="https://fonts.googleapis.com/css2?family=Roboto+Slab:wght@400&display=swap">
<style>
  :root {
    --page: #ffffff;
    --slate: #636680;
    --blush: #f6d6e0;
    --blossom: #c98fb1;
    --blossom-deep: #b27a9c;
  }
  html, body {
    margin: 0;
    padding: 0;
    width: 1110px;
    height: 1200px;
    overflow: hidden;
    background: var(--page);
  }
  .canvas {
    position: relative;
    width: 1110px;
    height: 1200px;
  }
  .label {
    position: absolute;
    left: 191px;
    top: 198px;
    width: 701px;
    height: 801px;
    background: var(--slate);
    font-family: "Roboto Slab", Georgia, serif;
    color: var(--blush);
  }
  .blossoms {
    position: absolute;
    left: -20px;
    top: -20px;
    width: 741px;
    height: 841px;
  }
  .company {
    position: absolute;
    top: 66px;
    left: 0;
    right: 0;
    margin: 0;
    text-align: center;
    font-size: 27px;
    font-weight: 400;
    letter-spacing: 0.5px;
  }
  .brand {
    position: absolute;
    top: 150px;
    left: 50%;
    transform: translateX(-50%);
    margin: 0;
    writing-mode: vertical-rl;
    text-orientation: upright;
    font-size: 58px;
    font-weight: 400;
    line-height: 1;
    letter-spacing: 8px;
    color: var(--blush);
  }
  .tagline {
    position: absolute;
    top: 692px;
    left: 0;
    right: 0;
    margin: 0;
    text-align: center;
    font-size: 29px;
    font-weight: 400;
  }
</style>
</head>
<body>
  <div class="canvas">
    <section class="label">
      <svg class="blossoms" viewBox="0 0 741 841" role="img" aria-label="Scattered pink cherry blossom flowers framing the left and right edges of the label">
        <defs>
          <linearGradient id="blossom-fade" x1="0" y1="0" x2="0" y2="1">
            <stop offset="0" stop-color="var(--blossom)" stop-opacity="0.85"/>
            <stop offset="1" stop-color="var(--blossom-deep)" stop-opacity="0.55"/>
          </linearGradient>
        </defs>
        <path class="blossom-cluster-left" fill="url(#blossom-fade)"
          d="M20 20 H280 Q300 60 250 85 Q200 110 160 150 Q150 230 165 300 Q160 380 160 470 Q150 520 110 520 Q70 500 40 440 Q30 300 20 200 Z"/>
        <path class="blossom-cluster-right" fill="url(#blossom-fade)"
          d="M720 40 V640 Q690 660 665 610 Q690 540 670 480 Q640 430 650 320 Q640 230 640 170 Q600 140 595 90 Q630 50 720 40 Z"/>
        <circle class="blossom-single" cx="197" cy="550" r="20" fill="url(#blossom-fade)"/>
        <circle class="blossom-single" cx="72" cy="625" r="20" fill="url(#blossom-fade)"/>
        <circle class="blossom-single" cx="156" cy="738" r="19" fill="url(#blossom-fade)"/>
        <circle class="blossom-single" cx="287" cy="536" r="21" fill="url(#blossom-fade)"/>
        <circle class="blossom-single" cx="517" cy="37" r="22" fill="url(#blossom-fade)"/>
      </svg>

      <p class="company">Tall Casks</p>
      <h1 class="brand">Velmora</h1>
      <p class="tagline">premium Japanese sake</p>
    </section>
  </div>
</body>
</html>
```